2 Funky Pages + EASY stock logo = Construction Website

We would like a funky new website - Just 2 pages - to promote our project management company. A logo is also needed, but we'll provide a stock image which just needs a colour change a text added.

Here are the instructions:

"Fair Tally Homes"

#logo
The one I'd like is attached. Please change font and positioning of text though.

Tagline is "Don't be normal - Be clever"

#Colour combo
756897 Wood Veneer
D5D6D2 sand dollar
353C3F charcoal
962715 brick red

#Home - Page 1

Our cost-price home build service will save you thousands.
No, seriously - Here's how we do it (button)

- Pay what the home building companies do.
- FTH will manage the entire project.
- Use Keystonecraft Guaranteed builders and materials.
- Tender for the best industry rates.
- Get a full budget calculated for the build.
- Avoid inflated 'Fixed-price' builds.
See how it works (button)

Contact Us: 0800 615 278
enquire - Name, Phone, email, comment - SEND

#How it works - Page 2

Traditional fixed price contracts are popular because it means that any risk of unexpected problems is carried by the home builder, but the builder will generally load the price about 10 times above the actual risk carried.

It's like an over-priced insurance policy, on steroids.

Clever people do things differently.

Here's how a cost-price build works...

1) Tell us what you want to build. Dream home, townhouse, investment property, whatever.

2) We'll put a design together for you, or you can choose from a bunch of plans we've already got.

3) We'll give you a conservative price estimate.

4) We finish tweaking your plans, then send them out to our network of more than 200 builders, subcontractors and tradesmen.

5) We collect the quotes, pick the best prices, and finalise your budget. Now you buy us beer, cause you've finally realised how much you're saving.

6) Tell your friends how awesome we are, while we lodge your building consent application with Council.

7) We coordinate the builders and subbies (look, you're already speaking trade-talk) from start to finish. You pay the cost price on their work each month.

We're happy to talk numbers and give you an estimate.

Contact Us: 0800 615 278

Reason: I have seen some great design elements, but need them to come together in one site design. Also, there appears to be less attention paid to the second page design ('how it works') than is necessary... There is no viable contender there yet, compared with the great home page submissions. I've also added some further info to the brief, and note that many submissions have ignored the colour combo I've requested.

Industry/Entity Type

Construction

Number of Pages Required

2 page

Requirements
Must have
• Keystonecrafter logo (small)
• Colour combo described in brief.
Nice to have
• I've attached a stock image I like, but it's certainly not essential. I do like images with clear backgrounds though - they tend to produce a crisp looking site.
• There is a wider image similar to this, available on Pixel Vault, but Sketch Hive won't let me attach it.
Should not have
• Photos of cheesy American faces.

```html
<!DOCTYPE html>
<html lang="en">
<head>
<meta charset="utf-8">
<title>Fair Tally Homes</title>
<link href="https://fonts.googleapis.com/css2?family=Open+Sans:ital,wght@0,400;0,600;0,700;0,800;1,700;1,800&display=swap" rel="stylesheet">
<style>
:root{
  --wood:#756897;
  --wood-dark:#4f446f;
  --sand:#d5d6d2;
  --charcoal:#353c3f;
  --brick:#962715;
  --white:#ffffff;
  --ink:#2a2a2a;
  --paper:#f4f4f4;
  --black:#0d0d0d;
}
*{box-sizing:border-box;margin:0;padding:0}
html,body{width:1200px;height:4337px;overflow:hidden}
body{position:relative;background:var(--white);font-family:"Open Sans",Arial,sans-serif;color:var(--ink)}
.ph{position:absolute}
.btn-red{position:absolute;background:var(--brick);color:var(--white);font-weight:700;display:flex;align-items:center;justify-content:center;text-transform:uppercase;white-space:nowrap}

/* header */
.site-header{position:absolute;left:0;top:0;width:1200px;height:92px;background:var(--white)}
.brand{position:absolute;left:174px;top:18px;display:flex;align-items:center;gap:12px}
.brand-square{width:52px;height:52px;background:var(--wood);flex:none}
.brand-name{color:var(--brick);font-weight:700;font-size:24px;line-height:26px;text-transform:uppercase}
.contact-box{position:absolute;top:12px;height:66px;border:4px solid var(--wood-dark);padding:8px 14px 0 60px}
.contact-box svg{position:absolute;left:16px;top:16px}
.contact-box b{display:block;font-size:15px;font-weight:800;color:var(--ink);text-transform:uppercase}
.contact-box span{font-size:13px;color:var(--ink)}

.main-nav{position:absolute;left:168px;top:92px;width:862px;height:47px;background:var(--wood);display:flex;align-items:center;padding-left:16px;gap:22px}
.main-nav a{color:var(--white);font-size:13px;font-weight:700;text-decoration:none;text-transform:uppercase}
.main-nav .nav-cta{position:absolute;right:0;top:0;height:47px;width:162px;background:var(--brick);display:flex;align-items:center;justify-content:center;gap:8px}

/* hero */
.hero{position:absolute;left:0;top:139px;width:1200px;height:439px;background:linear-gradient(110deg,#e9e7e2 0%,#cfcac0 45%,#a99e90 70%,#dedbd5 100%)}
.hero-line1{position:absolute;left:0;width:1200px;top:320px;text-align:center;color:var(--white);font-size:36px;font-weight:600;text-transform:uppercase;line-height:44px}
.hero-line2{position:absolute;left:247px;width:706px;top:364px;height:50px;background:rgba(53,60,63,.75);color:var(--white);font-size:34px;font-weight:800;text-transform:uppercase;text-align:center;line-height:50px}

/* welcome */
.welcome-title{position:absolute;left:150px;top:615px;width:275px;text-align:right;color:var(--charcoal);font-size:22px;line-height:26px;text-transform:uppercase;font-weight:600}
.welcome-title strong{font-weight:800}
.welcome-rule{position:absolute;left:448px;top:605px;width:2px;height:110px;background:var(--charcoal)}
.welcome-text{position:absolute;left:486px;top:610px;width:560px;font-size:16px;line-height:21px;font-weight:700;font-style:italic;color:var(--charcoal)}

/* about */
.about-photo{left:0;top:746px;width:599px;height:382px;background:linear-gradient(135deg,#b79a6c,#e8dfd2 50%,#8d8677)}
.since-tag{position:absolute;left:318px;top:800px;width:281px;height:40px;background:var(--brick);color:var(--white);font-size:21px;letter-spacing:1px;display:flex;align-items:center;justify-content:center;text-transform:uppercase}
.about-panel{position:absolute;left:599px;top:746px;width:601px;height:382px;background:var(--charcoal);color:var(--white);padding:30px 56px 0 64px}
.about-panel h2{font-size:24px;font-weight:800;text-transform:uppercase}
.about-panel h2::after{content:"";display:block;width:60px;height:3px;background:var(--brick);margin-top:8px}
.about-panel p{font-size:14px;margin-top:12px;font-weight:600}
.about-list{display:grid;grid-template-columns:1fr 1fr;gap:12px 26px;margin-top:18px;list-style:none}
.about-list li{font-size:12px;padding-left:18px;position:relative;line-height:16px}
.about-list li::before{content:"";position:absolute;left:0;top:4px;width:8px;height:8px;background:var(--brick)}
.about-btns{position:absolute;left:56px;top:278px;display:flex;gap:12px}
.about-btns div{position:static;height:38px;padding:0 14px;font-size:15px;text-transform:none;font-weight:600}

/* services */
.services{position:absolute;left:0;top:1128px;width:1200px;height:405px;background:var(--paper)}
.service{position:absolute;width:425px;height:130px;background:var(--white)}
.service-img{position:absolute;left:0;top:0;width:130px;height:130px;border:4px solid var(--wood)}
.service h3{position:absolute;left:150px;top:16px;font-size:16px;font-weight:800;text-transform:uppercase}
.service h3::after{content:"";display:block;width:26px;height:3px;background:var(--wood);margin-top:6px}
.service p{position:absolute;left:150px;top:56px;width:260px;font-size:11px;line-height:14px;color:#555}

/* support band */
.support{position:absolute;left:0;top:1533px;width:1200px;height:144px;background:var(--wood)}
.support h2{position:absolute;left:174px;top:42px;color:var(--white);font-size:34px;font-style:italic;font-weight:800}
.support p{position:absolute;left:174px;top:90px;color:#ece8f4;font-size:12px}
.support .btn-red{left:775px;top:58px;width:179px;height:37px;font-size:13px}

/* how it works */
.how{left:0;top:1677px;width:1200px;height:796px;background:linear-gradient(160deg,#8b8f93,#6d7276 50%,#8f8a80)}
.how-tag{position:absolute;left:81px;top:1706px;width:252px;height:47px;background:var(--brick);color:var(--white);font-size:24px;display:flex;align-items:center;padding-left:16px;text-transform:uppercase}
.how-text{position:absolute;left:81px;top:1768px;width:590px;color:var(--white);font-size:15.5px;line-height:19px}
.how-text p{margin-bottom:13px}
.how-text p.tight{margin-bottom:0}
.how-contact{left:81px;top:2380px;width:233px;height:38px;font-size:16px;text-transform:none;font-weight:600}
.appt{position:absolute;left:694px;top:1831px;width:428px;height:470px;background:var(--white);padding:26px 28px}
.appt h4{font-size:13px;font-weight:800;text-transform:uppercase;border-left:4px solid var(--brick);padding-left:10px;margin-bottom:28px;margin-left:16px}
.appt label{display:block;font-size:10px;font-weight:700;text-transform:uppercase;margin-top:12px}
.appt .field{height:34px;border:1px solid #ccc;margin-top:5px;font-size:10px;color:#999;padding:10px}
.appt .field.area{height:62px}
.appt .send{position:relative;margin-top:18px;width:66px;height:24px;font-size:10px}

/* portfolio */
.portfolio{position:absolute;left:0;top:2473px;width:1200px;height:616px;background:var(--sand)}
.sec-title{position:absolute;left:0;width:1200px;text-align:center;font-size:22px;font-weight:800;text-transform:uppercase;color:var(--ink)}
.sec-sub{position:absolute;left:300px;width:600px;text-align:center;font-size:11px;line-height:15px;color:#333}
.filters{position:absolute;left:0;width:1200px;top:121px;display:flex;justify-content:center;gap:8px}
.filters span{border:2px solid var(--brick);background:var(--white);font-size:11px;font-weight:700;padding:4px 12px;text-transform:uppercase}
.filters span.on{background:var(--sand)}
.tile{position:absolute;width:213px;height:182px;border:4px solid var(--brick)}

/* testimonials */
.testi{left:0;top:3089px;width:1200px;height:289px;background:linear-gradient(120deg,#7c7874,#5e6266 60%,#9c9384)}
.testi-title{position:absolute;left:0;width:1200px;top:3122px;text-align:center;color:var(--white);font-size:22px;font-weight:800;text-transform:uppercase}
.testi-name{position:absolute;left:486px;top:3170px;width:223px;height:62px;border:3px solid var(--brick);background:rgba(53,60,63,.6);color:var(--white);text-align:center;padding-top:8px}
.testi-name b{display:block;font-size:20px}
.testi-name span{font-size:11px}
.dots{position:absolute;left:580px;top:3244px;display:flex;gap:6px}
.dots i{width:7px;height:7px;border-radius:50%;background:#bbb;display:block}
.dots i.on{background:var(--white)}
.testi-quote{position:absolute;left:170px;width:860px;top:3270px;text-align:center;color:var(--white);font-size:12px;line-height:28px;font-style:italic;font-weight:700}

/* news */
.news{position:absolute;left:0;top:3378px;width:1200px;height:590px;background:var(--sand)}
.news-card{position:absolute;top:156px;width:269px}
.news-img{position:absolute;left:0;top:0;width:269px;height:176px}
.news-date{position:absolute;left:0;top:188px;width:44px;height:52px;background:var(--brick);color:var(--white);text-align:center;font-weight:800;font-size:18px;padding-top:5px;line-height:20px}
.news-date small{display:block;font-size:9px}
.news-head{position:absolute;left:56px;top:188px;font-size:15px;line-height:19px;width:200px}
.news-meta{position:absolute;left:56px;top:228px;font-size:10px;color:#444}
.news-body{position:absolute;left:0;top:262px;width:260px;font-size:14px;font-weight:700;line-height:18px}
.news-more{position:absolute;left:0;top:332px;font-size:11px;color:#333}

/* footer */
.site-footer{position:absolute;left:0;top:3968px;width:1200px;height:369px;background:var(--black);color:var(--white)}
.foot-brand{position:absolute;left:174px;top:36px;display:flex;gap:10px;align-items:center}
.foot-brand .brand-square{width:44px;height:44px}
.foot-brand .brand-name{color:var(--white);font-size:19px;line-height:21px}
.foot-about{position:absolute;left:174px;top:104px;width:200px;font-size:12px;font-weight:700;line-height:16px}
.foot-social{position:absolute;left:174px;top:226px;display:flex;gap:14px}
.foot-social i{width:14px;height:14px;border-radius:50%;background:var(--white);display:block}
.foot-col h5{font-size:15px;font-weight:800;margin-bottom:14px}
.foot-col{position:absolute;top:40px}
.foot-news{display:flex;gap:10px;margin-bottom:12px}
.foot-news div{width:48px;height:34px;background:linear-gradient(135deg,#3b6da4,#d59b4a);flex:none}
.foot-news p{font-size:10px;line-height:13px;width:120px}
.foot-links p{font-size:12px;font-weight:700;line-height:22px}
.gallery{display:grid;grid-template-columns:repeat(4,46px);gap:6px}
.gallery div{height:34px;background:linear-gradient(135deg,#3b6da4,#d59b4a)}
.subscribe{display:flex;margin-top:6px}
.subscribe .inp{width:190px;height:30px;background:var(--white);color:#999;font-size:10px;padding:8px}
.subscribe .go{width:40px;height:30px;background:var(--wood);display:flex;align-items:center;justify-content:center}
.copyright{position:absolute;left:0;width:1200px;top:332px;text-align:center;font-size:12px}
</style>
</head>
<body>

<header class="site-header">
  <div class="brand">
    <div class="brand-square"></div>
    <div class="brand-name">Fair Tally<br>Homes</div>
  </div>
  <div class="contact-box" style="left:564px;width:217px">
    <svg width="30" height="30" viewBox="0 0 24 24"><path fill="#353c3f" d="M6.6 10.8a15 15 0 0 0 6.6 6.6l2.2-2.2c.3-.3.7-.4 1-.2 1.1.4 2.3.6 3.6.6.6 0 1 .4 1 1V20c0 .6-.4 1-1 1A17 17 0 0 1 3 4c0-.6.4-1 1-1h3.5c.6 0 1 .4 1 1 0 1.3.2 2.5.6 3.6.1.3 0 .7-.2 1z"/></svg>
    <b>Call now</b><span>0800 615 278</span>
  </div>
  <div class="contact-box" style="left:795px;width:232px">
    <svg width="30" height="30" viewBox="0 0 24 24"><path fill="#353c3f" d="M3 5h18v14H3zM4 6.5v.3l8 5.4 8-5.4v-.3z"/></svg>
    <b>Email</b><span>hello@fairtally.example</span>
  </div>
</header>

<nav class="main-nav">
  <a>Home</a><a>About us</a><a>Services</a><a>Portfolio</a><a>Pricing</a><a>Team</a><a>Blog</a><a>Contact us</a>
  <a class="nav-cta"><svg width="12" height="12" viewBox="0 0 12 12"><path d="M1 6l3 3 7-7" stroke="#fff" stroke-width="2" fill="none"/></svg>How we do it</a>
</nav>

<section class="hero" role="img" aria-label="Two builders in hard hats reviewing plans on a bright site"></section>
<div class="hero-line1">Our cost-price home build</div>
<div class="hero-line2">Service will save you thousands.</div>
<div class="btn-red" style="left:491px;top:424px;width:217px;height:40px;font-size:17px">How we do it</div>

<h2 class="welcome-title">Wecome to<br><strong>Keystonecrafters</strong></h2>
<div class="welcome-rule"></div>
<p class="welcome-text">Lorem ipsum dolor sit amet, cons ectetur elit. Vestib ulum nec odios Suspe ndisse cursus mal suada fact lisis. Lorem ipsum dolor sit. Lorem ipsum dolor sit amet, cons ectetur elit. Vestib ulum nec odios Suspe ndisse cursus mal suada fact lisis. Lorem ipsum dolor sit.</p>

<div class="ph about-photo" role="img" aria-label="Smiling builder in a yellow hard hat on site"></div>
<div class="since-tag">We are since year</div>
<section class="about-panel">
  <h2>We are Keystonecrafters</h2>
  <p>Our cost-price home build service will save you thousands.</p>
  <ul class="about-list">
    <li>Pay what the home building companies do.</li>
    <li>Tender for the best industry rates.</li>
    <li>FTH will manage the entire project.</li>
    <li>Get a full budget calculated for the build.</li>
    <li>Use Keystonecraft Guaranteed builders and materials.</li>
    <li>Avoid inflated 'Fixed-price' builds.</li>
  </ul>
  <div class="about-btns"><div class="btn-red">How it works</div><div class="btn-red">Contact Us : 0800 615 278</div></div>
</section>

<section class="services">
  <div class="service" style="left:168px;top:72px"><div class="service-img" role="img" aria-label="Builders at work" style="background:linear-gradient(135deg,#3e6fb0,#e2b64a)"></div><h3>Construstion</h3><p>Ves tibulum nec odios Suspe ndisse cursus mal suada tibulum nec odios Suspe ndisse cursus mal suada fact lisis. Lorem ipsum dolor.</p></div>
  <div class="service" style="left:607px;top:72px"><div class="service-img" role="img" aria-label="Designer holding interior plans" style="background:linear-gradient(135deg,#d8d3c8,#8a7a62)"></div><h3>Interior design package</h3><p>Ves tibulum nec odios Suspe ndisse cursus mal suada tibulum nec odios Suspe ndisse cursus mal suada fact lisis. Lorem ipsum dolor.</p></div>
  <div class="service" style="left:168px;top:223px"><div class="service-img" role="img" aria-label="Team reviewing renovation drawings" style="background:linear-gradient(135deg,#c6c1b5,#5c6b80)"></div><h3>Renovation</h3><p>Ves tibulum nec odios Suspe ndisse cursus mal suada tibulum nec odios Suspe ndisse cursus mal suada fact lisis. Lorem ipsum dolor.</p></div>
  <div class="service" style="left:607px;top:223px"><div class="service-img" role="img" aria-label="Worker carrying timber flooring" style="background:linear-gradient(135deg,#b9542e,#e8b37a)"></div><h3>Hardwood flooring</h3><p>Ves tibulum nec odios Suspe ndisse cursus mal suada tibulum nec odios Suspe ndisse cursus mal suada fact lisis. Lorem ipsum dolor.</p></div>
</section>

<section class="support">
  <h2>24/7 Supports For all Membership</h2>
  <p>Lorem ipsum dolor sit amet, Lorem ipsum dolor cons ectetur elit. Ves tibulum nec odios.</p>
  <div class="btn-red">See all package</div>
</section>

<section class="ph how" role="img" aria-label="Builder's hands over blueprints with tools"></section>
<div class="how-tag">How it works</div>
<div class="how-text">
  <p>Traditional fixed price contracts are popular because it means that any risk of unexpected problems is carried by the home builder, but the builder will generally load the price about 10 times above the actual risk carried.</p>
  <p class="tight">It's like an over-priced insurance policy, on steroids.</p>
  <p class="tight">Clever people do things differently.</p>
  <p>Here's how a cost-price build works...</p>
  <p>1) Tell us what you want to build. Dream home, townhouse, investment property, whatever.</p>
  <p>2) We'll put a design together for you, or you can choose from a bunch of plans we've already got.</p>
  <p>3) We'll give you a conservative price estimate.</p>
  <p>4) We finish tweaking your plans, then send them out to our network of more than 200 builders, subcontractors and tradesmen.</p>
  <p>5) We collect the quotes, pick the best prices, and finalise your budget. Now you buy us beer, cause you've finally realised how much you're saving.</p>
  <p>6) Tell your friends how awesome we are, while we lodge your building consent application with Council.</p>
  <p>7) We coordinate the builders and subbies (look, you're already speaking trade-talk) from start to finish. You pay the cost price on their work each month.</p>
  <p>We're happy to talk numbers and give you an estimate.</p>
</div>
<div class="btn-red how-contact">Contact Us : 0800 615 278</div>
<form class="appt">
  <h4>Get an appointment</h4>
  <label>Full name</label><div class="field">Your Name</div>
  <label>Phone</label><div class="field">Your Phone</div>
  <label>Email</label><div class="field">Your Email</div>
  <label>Comment</label><div class="field area">Your Comment</div>
  <div class="btn-red send">Submit</div>
</form>

<section class="portfolio">
  <div class="sec-title" style="top:30px">Portfolio</div>
  <p class="sec-sub" style="top:68px">Lorem ipsum dolor sit amet, cons ectetur elit. Ves tibulum nec odios Suspe ndisse cursus mal suada faci lisis. Lorem ipsum dolor.</p>
  <div class="filters"><span class="on">All</span><span>Indoor</span><span>Renovation</span><span>Hardwood</span><span>Isolation</span></div>
  <div class="tile" role="img" aria-label="Modern kitchen interior" style="left:159px;top:188px;background:linear-gradient(135deg,#e2ddd3,#7a6f62)"></div>
  <div class="tile" role="img" aria-label="Bright open-plan room" style="left:379px;top:188px;background:linear-gradient(135deg,#f2f2f0,#9aa3aa)"></div>
  <div class="tile" role="img" aria-label="Dark living room" style="left:599px;top:188px;background:linear-gradient(135deg,#6a6560,#1e1e1e)"></div>
  <div class="tile" role="img" aria-label="Warm lit retail interior" style="left:819px;top:188px;background:linear-gradient(135deg,#c79a64,#4b3a2c)"></div>
  <div class="tile" role="img" aria-label="Bedroom interior" style="left:159px;top:384px;background:linear-gradient(135deg,#d9c7a8,#8c6b4a)"></div>
  <div class="tile" role="img" aria-label="House among trees" style="left:379px;top:384px;background:linear-gradient(135deg,#6d8c5a,#2f4428)"></div>
  <div class="tile" role="img" aria-label="Large family home at dusk" style="left:599px;top:384px;background:linear-gradient(135deg,#6a8fb8,#c6a16c)"></div>
  <div class="tile" role="img" aria-label="Modern home with warm lights" style="left:819px;top:384px;background:linear-gradient(135deg,#a07452,#3a2a22)"></div>
</section>

<section class="ph testi" role="img" aria-label="Builders working on site"></section>
<div class="testi-title">What our clients say about us</div>
<div class="testi-name"><b>Miles Tarrant</b><span>Project Manager - Harbour Lane Ltd</span></div>
<div class="dots"><i></i><i class="on"></i><i></i></div>
<p class="testi-quote">We believe that analysis of your company and your customers is key in responding effectively to your promotional needs and we will work with you to fully understand your business to achieve the greatest amount of publicity possible so that you can see a return from the advertising.</p>

<section class="news">
  <div class="sec-title" style="top:40px">News</div>
  <p class="sec-sub" style="top:88px">Sed ut perspiciatis unde omnis iste natus error sit voluptatem accusa nt ium dolore mque laudantium totam rem aperiam</p>
  <article class="news-card" style="left:179px"><div class="news-img" role="img" aria-label="Colourful furnished living room" style="background:linear-gradient(135deg,#d88a3a,#6a4a2e)"></div><div class="news-date">22<small>MAR</small></div><div class="news-head">There will be short heading with img</div><div class="news-meta">♥ 3,156 &nbsp;&nbsp; 17 comments</div><p class="news-body">Lorem Ipsum is simply dummy text of the printing and typesetting industry.</p><div class="news-more">Read More →</div></article>
  <article class="news-card" style="left:463px"><div class="news-img" role="img" aria-label="Builder in hard hat on a roof" style="background:linear-gradient(135deg,#4c86c6,#e2a548)"></div><div class="news-date">22<small>MAR</small></div><div class="news-head">There will be short heading with img</div><div class="news-meta">♥ 3,156 &nbsp;&nbsp; 17 comments</div><p class="news-body">Lorem Ipsum is simply dummy text of the printing and typesetting industry.</p><div class="news-more">Read More →</div></article>
  <article class="news-card" style="left:746px"><div class="news-img" role="img" aria-label="Builder pointing at a building under a blue sky" style="background:linear-gradient(135deg,#7eaee0,#e6c86e)"></div><div class="news-date">22<small>MAR</small></div><div class="news-head">There will be short heading with img</div><div class="news-meta">♥ 3,156 &nbsp;&nbsp; 17 comments</div><p class="news-body">Lorem Ipsum is simply dummy text of the printing and typesetting industry.</p><div class="news-more">Read More →</div></article>
</section>

<footer class="site-footer">
  <div class="foot-brand"><div class="brand-square"></div><div class="brand-name">Fair Tally<br>Homes</div></div>
  <p class="foot-about">Lorem Ipsum is simply dummy text of the printing and typesetting industry. Lorem Ipsum has been the industry's standard dummy text ever since the printing and typesetting trade.</p>
  <div class="foot-social"><i></i><i></i><i></i><i></i><i></i><i></i></div>
  <div class="foot-col" style="left:390px"><h5>Latest News</h5>
    <div class="foot-news"><div></div><p>Lorem Ipsum is simply dummy text of the and industry<br>17 Jun, 2015</p></div>
    <div class="foot-news"><div></div><p>Lorem Ipsum is simply dummy text of the and industry<br>17 Jun, 2015</p></div>
    <div class="foot-news"><div></div><p>Lorem Ipsum is simply dummy text of the and industry<br>17 Jun, 2015</p></div>
  </div>
  <div class="foot-col foot-links" style="left:630px"><h5>Quick Links</h5><p>About us</p><p>Blog</p><p>About us</p><p>Portfolio</p><p>Our service</p><p>Logout FTH</p><p>FAQ</p></div>
  <div class="foot-col" style="left:758px"><h5>Gallery</h5>
    <div class="gallery"><div></div><div></div><div></div><div></div></div>
    <h5 style="margin-top:30px">Subscriber</h5>
    <div class="subscribe"><div class="inp">Enter your email here</div><div class="go"><svg width="14" height="14" viewBox="0 0 14 14"><path d="M1 7l12-6-4 12-2-5z" fill="#fff"/></svg></div></div>
  </div>
  <div class="copyright">Copyright © 2015. All rights reserved.</div>
</footer>

</body>
</html>
```